website design for a new age Real Estate Security Business

We are launching a business in real estate which no body else is doing. We are going to use technology in terms of software and hardware to provide our services.

We are going to use Big Data, IOT etc.. for our services.

NOTE: We don't want to see Shiel or buildings etc.. that directly suggests Real estate or security on this design

Target Market(s)

India

Industry/Entity Type

Real Estate

Number of Pages Required

4 page

Font styles to use
Sans Serif
Other font styles liked:
• Use Google Fonts

Requirements
Must have
• Home Page should be trendy and colourful should give user confidence to subscribe to our service.
Nice to have
• Use Google fonts.
Should not have
• Design shouldnt have Shield or Buildings that directly suggests real estate or security.

```html
<!DOCTYPE html>
<html lang="en">
<head>
<meta charset="utf-8">
<title>Data Analysis Action – Property Safety Services</title>
<link href="https://fonts.googleapis.com/css2?family=Rubik:wght@400;500&family=Roboto:wght@300;400;500;700&display=swap" rel="stylesheet">
<style>
:root{
  --ink:#22252c;
  --muted:#6b6f78;
  --amber:#fbb813;
  --teal:#05aaad;
  --coral:#fe6550;
  --soft:#f5f5f5;
  --night:#272c37;
  --night-text:#b8bcc6;
  --white:#ffffff;
}
*{box-sizing:border-box;margin:0;padding:0}
html,body{width:686px;height:1200px;overflow:hidden;background:var(--white)}
body{position:relative;font-family:'Roboto',sans-serif;color:var(--ink)}
.abs{position:absolute}

/* header */
.site-header{position:absolute;left:0;top:0;width:686px;height:52px;background:var(--white)}
.brand{left:50px;top:17px;font-family:'Rubik',sans-serif;font-weight:500;font-size:13px;color:var(--ink);display:flex;align-items:center;gap:6px}
.brand-dot{width:6px;height:6px;border-radius:50%;background:var(--amber)}
.main-nav{left:0;top:0;height:52px;width:686px}
.main-nav a{position:absolute;top:22px;font-size:6.8px;font-weight:500;color:var(--ink);text-decoration:none;letter-spacing:.1px}
.main-nav a.active{color:var(--amber)}
.active-bar{left:358px;top:0;width:30px;height:2px;background:var(--amber)}
.search-btn{left:613px;top:16px;width:21px;height:21px;border:1px solid #e3e3e3;border-radius:50%}

/* hero */
.hero{left:0;top:52px;width:686px;height:316px;
  background:radial-gradient(circle at 85% 10%,#4c7ad8 0%,rgba(60,100,200,0) 40%),
  linear-gradient(120deg,#071735 0%,#0f2f6b 40%,#1c4aa8 75%,#2456b8 100%)}
.hero-sub{left:0;width:686px;top:116px;text-align:center;color:#dbe3f5;font-weight:300;font-size:14.5px}
.hero-title{left:0;width:686px;top:134px;text-align:center;color:var(--white);font-family:'Rubik',sans-serif;font-weight:400;font-size:29px}
.btn-amber{background:var(--amber);color:var(--white);font-size:6px;font-weight:700;border-radius:13px;display:flex;align-items:center;justify-content:center;letter-spacing:.2px}
.hero-btn{left:303px;top:174px;width:82px;height:24px}
.slider-nav{left:648px;top:108px;width:26px;color:var(--white);font-size:8px;font-weight:700;text-align:center}
.slider-nav span{position:absolute;left:0;width:26px}
.slider-nav .current{color:var(--amber);font-size:10px}
.scroll-down{left:331px;top:355px;width:24px;height:24px;border-radius:50%;background:var(--white);box-shadow:0 2px 6px rgba(0,0,0,.15)}

/* services */
.services{left:0;top:368px;width:686px;height:263px;background:var(--soft)}
.section-title{font-family:'Rubik',sans-serif;font-weight:500;font-size:17px;color:var(--ink)}
.services .section-title{left:0;width:686px;top:38px;text-align:center}
.service-card{top:74px;width:273px;height:149px;background:var(--white);box-shadow:0 1px 4px rgba(0,0,0,.05)}
.service-media{left:0;top:0;width:131px;height:149px}
.service-body{left:149px;top:19px;width:118px}
.service-body h3{font-family:'Roboto',sans-serif;font-weight:500;font-size:9.5px;margin-top:44px;color:var(--ink)}
.service-body p{font-size:6.3px;line-height:11px;color:var(--muted);margin-top:7px}
.read-more{display:flex;align-items:center;gap:4px;margin-top:8px;font-size:5.6px;font-weight:500;color:var(--amber)}

/* pricing */
.plan{top:672px;width:152px;height:226px;color:var(--white);text-align:center}
.plan-doc{left:50px;background:var(--teal)}
.plan-land{left:217px;background:var(--coral)}
.plan-tab{left:0;top:17px;width:111px;height:22px;background:var(--white);border-radius:0 11px 11px 0;font-size:8px;display:flex;align-items:center;justify-content:center}
.plan-doc .plan-tab{color:var(--teal)}
.plan-land .plan-tab{color:var(--coral)}
.plan-price{left:0;top:58px;width:152px;font-family:'Roboto',sans-serif;font-weight:700;font-size:24px;display:flex;justify-content:center;align-items:baseline;gap:3px;padding-left:6px}
.plan-price small{font-size:5.5px;font-weight:400}
.plan-features{left:0;top:103px;width:152px;list-style:none;font-size:6.8px}
.plan-features li{height:18.5px}
.plan-view{left:53px;top:190px;width:46px;height:21px;border-radius:11px;background:rgba(255,255,255,.18);font-size:5.8px;font-weight:700;display:flex;align-items:center;justify-content:center}
.pricing-intro{left:426px;top:752px;width:214px}
.pricing-intro p{margin-top:9px;font-size:6.6px;line-height:12.5px;color:var(--muted)}

/* footer */
.footer-bg{left:0;top:930px}
.newsletter{left:95px;top:940px;width:495px;height:62px;background:var(--white);border-radius:31px;box-shadow:0 6px 18px rgba(0,0,0,.12)}
.newsletter h2{position:absolute;left:28px;top:20px;font-family:'Rubik',sans-serif;font-weight:500;font-size:15px}
.newsletter-field{left:142px;top:18px;width:262px;height:25px;background:#f2f2f3;border-radius:13px 0 0 13px;font-size:5.6px;color:#9a9ea6;display:flex;align-items:center;padding-left:15px;gap:6px}
.newsletter-submit{left:404px;top:18px;width:67px;height:25px;border-radius:0 13px 13px 0;background:var(--amber);color:var(--white);font-size:5.8px;font-weight:700;display:flex;align-items:center;justify-content:center}
.footer-heading{font-size:8.3px;font-weight:500;color:var(--white)}
.footer-list{list-style:none;font-size:6.6px;color:var(--night-text)}
.footer-list li{height:20.3px;display:flex;align-items:flex-start;gap:5px}
.ico-square{width:6px;height:6px;background:var(--night-text);border-radius:1px;margin-top:1px;flex:none}
.copyright{left:0;width:686px;top:1178px;text-align:center;font-size:6.4px;color:var(--night-text)}
.to-top{left:651px;top:1155px;width:20px;height:20px;border-radius:50%;background:var(--white)}
</style>
</head>
<body>

<header class="site-header">
  <div class="abs active-bar"></div>
  <div class="abs brand"><span class="brand-dot"></span>Logo Here</div>
  <nav class="abs main-nav">
    <a class="active" style="left:365px">HOME</a>
    <a style="left:403px">ABOUT US</a>
    <a style="left:455px">SERVICES</a>
    <a style="left:505px">PRICING</a>
    <a style="left:551px">CONTACT US</a>
  </nav>
  <div class="abs search-btn">
    <svg width="21" height="21" viewBox="0 0 21 21"><circle cx="9.5" cy="9.5" r="2.6" fill="none" stroke="#9a9ea6" stroke-width=".8"/><line x1="11.4" y1="11.4" x2="13" y2="13" stroke="#9a9ea6" stroke-width=".8"/></svg>
  </div>
</header>

<section class="abs hero" role="img" aria-label="Blue network graphic of connected points and translucent triangles">
  <div class="abs hero-sub">Data Analysis Action</div>
  <h1 class="abs hero-title">To keep Your Property Safe</h1>
  <div class="abs btn-amber hero-btn">LEARN MORE</div>
  <div class="abs slider-nav">
    <span style="top:50px"><svg width="8" height="10" viewBox="0 0 8 10"><path d="M4 9V1M1 4l3-3 3 3" stroke="#fff" fill="none" stroke-width="1"/></svg></span>
    <span style="top:72px">01</span>
    <span class="current" style="top:93px">02</span>
    <span style="top:120px">03</span>
    <span style="top:141px"><svg width="8" height="10" viewBox="0 0 8 10"><path d="M4 1v8M1 6l3 3 3-3" stroke="#fff" fill="none" stroke-width="1"/></svg></span>
  </div>
</section>

<section class="abs services">
  <h2 class="abs section-title">Services We Provide</h2>

  <article class="abs service-card" style="left:51px">
    <div class="abs service-media" role="img" aria-label="Photo of a woman reading a document folder" style="background:linear-gradient(135deg,#eef0f0,#c9cccd 60%,#8a8c8e)"></div>
    <div class="abs service-body">
      <svg class="abs" style="left:0;top:0" width="28" height="34" viewBox="0 0 28 34"><path d="M2 1h14l7 7v20H2z" fill="none" stroke="#b5b8be" stroke-width="1"/><path d="M16 1v7h7M6 14h12M6 18h12M6 22h8" fill="none" stroke="#b5b8be" stroke-width="1"/><rect x="17" y="25" width="9" height="7" fill="#fff" stroke="#b5b8be"/><path d="M19 25v-2a2.5 2.5 0 0 1 5 0v2" fill="none" stroke="#b5b8be"/></svg>
      <h3>Doc Secure</h3>
      <p>This is Phot shop version &nbsp;of Lorem Ipsum proin gravida nibh vel vlit au ctor aliquet aenean...</p>
      <div class="read-more">READ MORE <svg width="10" height="6" viewBox="0 0 10 6"><path d="M0 3h9M6.5 .5 9 3 6.5 5.5" fill="none" stroke="#fbb813" stroke-width=".9"/></svg></div>
    </div>
  </article>

  <article class="abs service-card" style="left:362px">
    <div class="abs service-media" role="img" aria-label="Photo of a house under a blue sky on green lawn" style="background:linear-gradient(180deg,#6fb0e4 0%,#bcdaf1 45%,#9a8c86 62%,#6fa546 80%,#5e9a3c 100%)"></div>
    <div class="abs service-body">
      <svg class="abs" style="left:0;top:0" width="32" height="32" viewBox="0 0 32 32"><path d="M2 14 16 2l14 12v16H2z" fill="none" stroke="#b5b8be" stroke-width="1"/><circle cx="16" cy="18" r="6" fill="none" stroke="#b5b8be"/><rect x="13" y="17" width="6" height="5" fill="none" stroke="#b5b8be"/></svg>
      <h3>Land Secure</h3>
      <p>This is Phot shop version &nbsp;of Lorem Ipsum proin gravida nibh vel vlit au ctor aliquet aenean...</p>
      <div class="read-more">READ MORE <svg width="10" height="6" viewBox="0 0 10 6"><path d="M0 3h9M6.5 .5 9 3 6.5 5.5" fill="none" stroke="#fbb813" stroke-width=".9"/></svg></div>
    </div>
  </article>
</section>

<div class="abs btn-amber scroll-down" style="background:#fff">
  <svg width="8" height="9" viewBox="0 0 8 9"><path d="M4 0v8M1.5 5.5 4 8l2.5-2.5" stroke="#555" fill="none" stroke-width=".8"/></svg>
</div>

<article class="abs plan plan-doc">
  <div class="abs plan-tab">DOC SECURE</div>
  <div class="abs plan-price">3,99$ <small>Per Month</small></div>
  <ul class="abs plan-features">
    <li>Sollicitudin lorem</li><li>Quis bibendum auctor</li><li>Consequat ipsum</li><li>Nec sagittis sem nibh</li>
  </ul>
  <div class="abs plan-view">VIEW</div>
</article>

<article class="abs plan plan-land">
  <div class="abs plan-tab">LAND SECURE</div>
  <div class="abs plan-price">6,99$ <small>Per Month</small></div>
  <ul class="abs plan-features">
    <li>Sollicitudin lorem</li><li>Quis bibendum auctor</li><li>Consequat ipsum</li><li>Nec sagittis sem nibh</li>
  </ul>
  <div class="abs plan-view">VIEW</div>
</article>

<div class="abs pricing-intro">
  <h2 class="section-title">Services Pricing Plan</h2>
  <p>sollicitudin lorem quis bibendum auctor nisi elit consequat ipsu nec sagittis sem nibh id elit duis sed odio sit amet nibh vulputate cursus a sit amet mauris....</p>
</div>

<footer>
  <svg class="abs footer-bg" width="686" height="270" viewBox="0 0 686 270"><path d="M0 45 Q343 -10 686 45 V270 H0z" fill="#272c37"/></svg>

  <div class="abs newsletter">
    <h2>Newsletter</h2>
    <div class="abs newsletter-field"><svg width="7" height="5" viewBox="0 0 7 5"><rect x=".4" y=".4" width="6.2" height="4.2" fill="none" stroke="#9a9ea6" stroke-width=".6"/><path d="M.4.4 3.5 3 6.6.4" fill="none" stroke="#9a9ea6" stroke-width=".6"/></svg>Enter your email address..</div>
    <div class="abs newsletter-submit">SUBMIT</div>
  </div>

  <h3 class="abs footer-heading" style="left:50px;top:1037px">Quick Links</h3>
  <ul class="abs footer-list" style="left:50px;top:1060px"><li>› Home</li><li>› About Us</li><li>› Services</li><li>› Pricing</li></ul>
  <ul class="abs footer-list" style="left:117px;top:1060px"><li>› Contact Us</li><li>› Login</li><li>› Register</li><li>› FAQ's</li></ul>

  <h3 class="abs footer-heading" style="left:254px;top:1037px">Contact Us</h3>
  <ul class="abs footer-list" style="left:254px;top:1060px">
    <li><svg width="7" height="7" viewBox="0 0 7 7"><path d="M1 .5 2.5 2 1.8 3a4 4 0 0 0 2.2 2.2L5 4.5 6.5 6 5.5 7C2.5 6.5.5 4.5 0 1.5z" fill="#fbb813"/></svg>+91 00000 41520</li>
    <li><svg width="7" height="6" viewBox="0 0 7 6"><rect y=".5" width="7" height="5" fill="#fbb813"/><path d="M0 .5 3.5 3.5 7 .5" fill="none" stroke="#272c37" stroke-width=".6"/></svg>hello@estatewarden.in</li>
    <li style="line-height:11px"><svg width="6" height="8" viewBox="0 0 6 8" style="flex:none;margin-top:1px"><path d="M3 8C1 5.5 0 4 0 3a3 3 0 0 1 6 0c0 1-1 2.5-3 5z" fill="#fbb813"/><circle cx="3" cy="3" r="1" fill="#272c37"/></svg><span>Some Address line goes here,<br>City name, Country name</span></li>
  </ul>

  <h3 class="abs footer-heading" style="left:472px;top:1037px">Follow us on socail media</h3>
  <ul class="abs footer-list" style="left:472px;top:1060px">
    <li><span class="ico-square"></span>Friendwall</li>
    <li style="color:var(--amber)"><span class="ico-square" style="background:var(--amber)"></span>Chirper</li>
    <li><span class="ico-square"></span>Pinboard</li>
    <li><span class="ico-square"></span>Snapframe</li>
  </ul>
  <ul class="abs footer-list" style="left:536px;top:1060px">
    <li><span class="ico-square"></span>Vidstream</li>
    <li><span class="ico-square"></span>Workline</li>
  </ul>

  <div class="abs copyright">© 2017, All Rights Reserved.</div>
  <div class="abs to-top"><svg width="20" height="20" viewBox="0 0 20 20"><path d="M10 14V6M7.5 8.5 10 6l2.5 2.5" stroke="#272c37" fill="none" stroke-width=".9"/></svg></div>
</footer>

</body>
</html>
```